Fatigued and Overloaded by COVID Messages? We need original illustrations to show that.

Everywhere you look there are messages about COVID. That is leading many people to feel fatigued and overloaded by the messages.

We surveyed U.S. adults March 20th - 24th, 2020 and measured message fatigue, information overload, perceived repetition, and perceived exaggeration. Here is how participants responded:

When it comes to coronavirus . . .
55% feel exhausted by all the messages.
54% feel overloaded by the amount of information.
51% feel that the messages are repetitive.
47% feel like messages exaggerate how bad it is.

In other words, almost half of U.S. adults show signs of message fatigue, information overload, perceived message repetition, and perceived message exaggeration.

We will continue to survey 400 adults every week for the next 16 weeks. Each time we will measure message fatigue, information overload, perceived repetition, and perceived exaggeration. We expect that it will increase over time.

What are we looking for? We need innovative and original illustrations that attempt to communicate these findings. The illustrations would visualize message fatigue, information overload, perceived message repetition, and perceived message exaggeration.

What sort of visual are we looking for? Our preference is for an original illustration (or set of illustrations). Our preference is for creative and powerful illustrations, but we are also open to the creative and well-executed infographics.

We need these images fast . We will award monetary prizes to the 3 best designs. If we like more than that, then we might purchase more (e.g., in past contests, we have purchased as many as 30 designs).

What we will need:
(1) The illustrations must be original and we will need the photoshop and/or illustrator files for all artwork. (By original, we mean that the illustrations are 100% created by you. Our organization requires that we utilize only original illustrated work. We have had issues with free imagery being pirated and reposted as free. We sidestep that issue by just having everything created.)

(2) The illustration should say, somewhere: "Based on a survey of 400 U.S. adults conducted March 20 - 24th, 2020."

(3) We will have almost 4 months worth of data by the time this is done. In other words, the illustrations might be able to help us present that weekly data.

(4) We have conducted other Artquarry projects. It might be helpful to examine designs we liked in the past. For example, here is another COVID project we just finished:

https://jobs.artquarry-example.com/job/5172846

Target Market(s)

U.S. adults

Requirements
Must have
• Original illustrations. Mobile friendly design. People will view this on their smartphones.
Nice to have
• A design that we can use to communicate the data across time.

```html
<!DOCTYPE html>
<html lang="en">
<head>
<meta charset="utf-8">
<title>COVID Message Fatigue</title>
<link rel="stylesheet" href="https://fonts.googleapis.com/css2?family=Fredoka:wght@600&family=Cabin+Condensed:wght@600;700&display=swap">
<style>
  :root {
    --navy: #356a9a;
    --navy-deep: #2f5f8f;
    --header-light: #8fd3e6;
    --ink: #3a6591;
    --ink-dark: #1f2a5c;
    --track: #9bffff;
    --bar: #00ccff;
    --paper: #ffffff;
    --cream: #fffccc;
    --mint-a: #b3ece8;
    --mint-b: #c9fde0;
    --figure: #f3f08a;
  }
  * { margin: 0; padding: 0; box-sizing: border-box; }
  html, body { width: 1200px; height: 2289px; overflow: hidden; background: var(--paper); }
  .canvas { position: relative; width: 1200px; height: 2289px; overflow: hidden; background: var(--paper); }
  .backdrop { position: absolute; inset: 0; }
  .top-stripe { position: absolute; left: 0; top: 0; width: 1200px; height: 36px; background: var(--navy); }
  .header {
    position: absolute; left: 0; top: 52px; width: 1200px; height: 176px;
    background: linear-gradient(180deg, var(--navy) 0%, var(--navy-deep) 45%, var(--header-light) 100%);
    border-radius: 0 0 90px 90px;
    text-align: center;
  }
  .title {
    font-family: "Fredoka", sans-serif; font-weight: 600; font-size: 54px; line-height: 66px;
    color: #fff; padding-top: 20px; letter-spacing: 0.5px;
    -webkit-text-stroke: 1.5px #3b3b5a; paint-order: stroke fill;
  }
  .title .accent { color: #ff1a1a; -webkit-text-stroke: 2px #fff; }
  .subtitle {
    position: absolute; top: 240px; left: 0; width: 1200px; text-align: center;
    font-family: "Cabin Condensed", sans-serif; font-weight: 700; font-size: 52px; line-height: 67px;
    color: var(--ink);
  }
  .stat { position: absolute; left: 0; width: 1200px; }
  .stat-track { position: absolute; left: 295px; width: 813px; height: 165px; background: var(--track); }
  .stat-bar {
    position: absolute; left: 295px; height: 137px; background: var(--bar); border-radius: 0 16px 16px 0;
    font-family: "Cabin Condensed", sans-serif; font-weight: 700; font-size: 90px; color: #fff;
    text-align: right; padding-right: 20px; line-height: 137px;
  }
  .stat-label {
    position: absolute; left: 0; width: 1200px; text-align: center; padding-left: 205px;
    font-family: "Cabin Condensed", sans-serif; font-weight: 700; font-size: 54px; color: var(--ink);
    white-space: nowrap;
  }
  .figure { position: absolute; background: var(--figure); opacity: 0.55; border-radius: 40px; }
  .summary {
    position: absolute; left: 102px; top: 1769px; width: 994px; height: 384px; border-radius: 38px;
    background: linear-gradient(90deg, var(--mint-a), var(--mint-b));
    display: flex; align-items: center; justify-content: center; text-align: center;
    font-family: "Cabin Condensed", sans-serif; font-weight: 700; font-size: 48px; line-height: 66px;
    color: var(--ink-dark); padding: 0 50px;
  }
  .footer {
    position: absolute; left: 0; top: 2201px; width: 1200px; height: 88px; background: var(--navy);
    font-family: "Fredoka", sans-serif; font-weight: 600; font-size: 31px; color: #fff;
    display: flex; align-items: center; justify-content: center;
  }
</style>
</head>
<body>
<main class="canvas">
  <svg class="backdrop" width="1200" height="2289" viewBox="0 0 1200 2289" aria-hidden="true">
    <path fill="var(--cream)" d="M0 310 C120 350 200 420 215 560 C230 700 380 640 400 760 C410 860 470 900 500 1020 C520 1120 560 1200 650 1260 C760 1330 600 1460 420 1560 C330 1610 320 1720 420 1760 L1200 1770 L1200 2201 L0 2201 Z"/>
    <path fill="var(--cream)" d="M1060 1960 C1120 1990 1160 1960 1200 1930 L1200 2201 L1000 2201 Z"/>
  </svg>

  <div class="top-stripe"></div>
  <header class="header">
    <h1 class="title">Everywhere you look there are<br>messages about <span class="accent">COVID</span></h1>
  </header>
  <p class="subtitle">That is leading many people to feel fatigued<br>and overloaded by the messages</p>

  <div class="figure" role="img" aria-label="Stick figure slumped over a heavy speech bubble" style="left:60px;top:356px;width:190px;height:240px;"></div>
  <div class="stat-track" style="top:411px;"></div>
  <div class="stat-bar" style="top:425px;width:406px;">55%</div>
  <p class="stat-label" style="top:585px;">feel exhausted by all the messages</p>

  <div class="figure" role="img" aria-label="Stick figure bent under a large speech bubble" style="left:48px;top:775px;width:212px;height:150px;"></div>
  <div class="stat-track" style="top:762px;"></div>
  <div class="stat-bar" style="top:776px;width:398px;">54%</div>
  <p class="stat-label" style="top:937px;padding-left:80px;">feel overloaded by the amount of information</p>

  <div class="figure" role="img" aria-label="Frustrated stick figure holding head, surrounded by speech bubbles" style="left:44px;top:1075px;width:222px;height:245px;"></div>
  <div class="stat-track" style="top:1113px;"></div>
  <div class="stat-bar" style="top:1127px;width:370px;">51%</div>
  <p class="stat-label" style="top:1288px;">feel that the messages are repetitive</p>

  <div class="figure" role="img" aria-label="Doubtful stick figure shrugging beneath a speech bubble" style="left:54px;top:1368px;width:200px;height:320px;"></div>
  <div class="stat-track" style="top:1465px;"></div>
  <div class="stat-bar" style="top:1479px;width:331px;">47%</div>
  <p class="stat-label" style="top:1640px;padding-left:105px;">feel like messages exaggerate how bad it is</p>

  <section class="summary">
    <p>In other words, almost half of U.S. adults show signs of message fatigue, information overload, perceived message repetition, and perceived message exaggeration.</p>
  </section>

  <footer class="footer">Based on a survey of 400 U.S. adults conducted March 20 - 24th, 2020</footer>
</main>
</body>
</html>
```